PREMIUM AGENCY High End Business Card - A+++ Designers Wanted

** DO NOT ATTEMPT TO CONTACT ME THROUGH SEARCHING ON ZINTREL OR EMAILING ME THROUGH MY WEBSITE **

I need a fresh, contemporary business card designed using the logo attached (BRONSALK)

I have attached the font for BRONSALK

It must have a premium look and feel. The business card size must be STANDARD size.

You can submit either/both VERTICAL or HORIZONTAL designs.

FRONT: It must have the following sample information on

Paul Ardley
Director Operations
Mobile +61 452 118 906
Email paulardley@bronsalk.com
www.bronsalk.com

The REAR of the business card must have the words

CREATE INSPIRE TOMORROW

as part of the design, in the same font (NEXA) attached.

The words do not need to be in capitals, or on the same line, please design this as you see it best working.

ADDITIONAL INFORMATION
======================

The BRONSALK logo must be on the front of the card

I want Ultraviolet printing on the final design, to enhance either the NAME of the person OR the BRONSALK logo OR the words on the back of the card.

Target Market(s)

Agency, Advertising Agency, Creative, Designers

Industry/Entity Type

Media

Contact Information for Business Card

Design Agency, Contemporary, Premium look and feel, High Quality

Font styles to use
Serif
Sans Serif
Other font styles liked:
• ATTACHED TO PROJECT

Requirements
Must have
• BLACK & WHITE as the primary design, and if you feel there can be a highlighted colour, then this can be used.
• The Logo ICON attached is blue, this colour must not be changed.
• I have attached the partner brand BRONSALK MEDIA incase you need to manipulate the original files.
• ** DO NOT ATTEMPT TO CONTACT ME THROUGH SEARCHING ON ZINTREL OR EMAILING ME THROUGH MY WEBSITE **
Nice to have
• Must be Premium. I have attached some sample designs, that I like that would be a good inspiration for where this can be taken.
• My favourite design is is the KESTRAVUE2-BUSINESSCARD-TEMPLATE
Should not have
• No funny or silly standard / off the shelf designs

```html
<!DOCTYPE html>
<html lang="en">
<head>
<meta charset="UTF-8">
<title>Bronsalk Media — Business Card Set</title>
<link rel="stylesheet" href="https://fonts.googleapis.com/css2?family=Montserrat:wght@400;500;800&family=Nunito:wght@300;400&display=swap">
<style>
  :root {
    --backdrop: #c9cacc;
    --card: #000000;
    --ink: #f2f2f2;
    --ink-soft: #d4d4d4;
    --accent: #2aa8dc;
    --mark-faint: #1c1c1c;
    --shadow: rgba(0, 0, 0, 0.35);
  }
  * { margin: 0; padding: 0; box-sizing: border-box; }
  html, body { width: 1200px; height: 1200px; overflow: hidden; }
  body {
    background: var(--backdrop);
    position: relative;
    font-family: "Nunito", sans-serif;
    color: var(--ink);
  }
  .card {
    position: absolute;
    background: var(--card);
    overflow: hidden;
    box-shadow: 4px 6px 10px var(--shadow);
  }
  .card--portrait { width: 365px; height: 606px; }
  .card--landscape { width: 607px; height: 364px; }
  .front-portrait { left: 203px; top: 65px; }
  .back-portrait { left: 635px; top: 65px; }
  .front-landscape { left: 94px; top: 709px; }
  .back-landscape { left: 503px; top: 770px; }

  .brand {
    position: absolute;
    display: flex;
    align-items: center;
    gap: 10px;
    font-family: "Montserrat", sans-serif;
    font-weight: 500;
    font-size: 21px;
    letter-spacing: 2.5px;
    color: var(--ink);
    white-space: nowrap;
  }
  .brand__dot {
    width: 14px; height: 14px;
    border-radius: 50%;
    background: var(--ink);
  }
  .person { position: absolute; }
  .person__name {
    font-family: "Montserrat", sans-serif;
    font-weight: 500;
    font-size: 24px;
    line-height: 1.2;
    letter-spacing: 0.3px;
  }
  .person__role {
    font-weight: 300;
    font-size: 26px;
    line-height: 1.3;
    color: var(--ink-soft);
  }
  .contact {
    position: absolute;
    list-style: none;
    font-weight: 300;
    font-size: 15px;
    line-height: 20px;
    color: var(--ink-soft);
  }
  .accent-band {
    position: absolute;
    left: 0; bottom: 0;
    width: 100%; height: 31px;
    background: var(--accent);
  }
  .mark-faint {
    position: absolute;
    width: 150px; height: 150px;
    border-radius: 50%;
    background: var(--mark-faint);
  }
  .motto {
    position: absolute;
    font-family: "Montserrat", sans-serif;
    font-weight: 800;
    font-size: 34px;
    line-height: 42px;
    text-align: center;
    letter-spacing: -0.5px;
    background: linear-gradient(180deg, #ffffff 0%, #9a9a9a 55%, #ffffff 100%);
    -webkit-background-clip: text;
    background-clip: text;
    color: transparent;
  }
  .motto span { display: block; }
</style>
</head>
<body>

  <section class="card card--portrait front-portrait">
    <div class="brand" style="left:37px; top:47px;"><span class="brand__dot"></span>BRONSALK MEDIA</div>
    <div class="person" style="left:37px; top:213px;">
      <p class="person__name">Paul Ardley</p>
      <p class="person__role">Director Operations</p>
    </div>
    <ul class="contact" style="left:37px; top:309px;">
      <li>Mobile +61 452 118 906</li>
      <li>Email paulardley@bronsalk.com</li>
      <li>www.bronsalk.com</li>
    </ul>
    <div class="mark-faint" role="img" aria-label="Faint brand mark" style="left:-30px; top:420px;"></div>
    <div class="accent-band"></div>
  </section>

  <section class="card card--portrait back-portrait">
    <p class="motto" style="left:0; width:100%; top:206px;">
      <span>“CREATE</span><span>INSPIRE</span><span>TOMORROW”</span>
    </p>
    <div class="mark-faint" role="img" aria-label="Faint brand mark" style="left:265px; top:420px;"></div>
  </section>

  <section class="card card--landscape front-landscape">
    <div class="brand" style="left:49px; top:45px;"><span class="brand__dot"></span>BRONSALK MEDIA</div>
    <div class="person" style="left:49px; top:138px;">
      <p class="person__name">Paul Ardley</p>
      <p class="person__role">Director Operations</p>
    </div>
    <ul class="contact" style="left:49px; top:236px;">
      <li>Mobile +61 452 118 906</li>
      <li>Email paulardley@bronsalk.com</li>
      <li>www.bronsalk.com</li>
    </ul>
    <div class="accent-band" style="height:30px;"></div>
  </section>

  <section class="card card--landscape back-landscape">
    <p class="motto" style="left:90px; width:410px; top:120px;">
      <span>“CREATE</span><span>INSPIRE</span><span>TOMORROW”</span>
    </p>
    <div class="mark-faint" role="img" aria-label="Faint brand mark" style="left:-20px; top:180px;"></div>
  </section>

</body>
</html>
```